Design of packaging box for vitamins

Hello,

need design of paper packaging box of pills (vitamins). Product itself (pills), will be put in the alu-blister, which will be put then into your designed box. Of course most important is eye-catching design, our idea is contrast colours, with chrome touch, or chrome framing..we are not designers, it´s your job :-). Name of the vitamin is B17 also called Laetrile or Amygdalin (both aliases should be displayed on the box). Text can be made by designer in english language, translation into our language will be done later with cooperation with designer.

```html
<!DOCTYPE html>
<html lang="en">
<head>
<meta charset="utf-8">
<title>Vitamin B17 Packaging</title>
<link rel="stylesheet" href="https://fonts.googleapis.com/css2?family=Montserrat:wght@600;700;800;900&family=Cinzel:wght@600;700&display=swap">
<style>
  :root{
    --bg:#e9e9e9;
    --white:#ffffff;
    --cream:#fffdf2;
    --yellow:#ffe34a;
    --amber:#ffb21a;
    --orange:#ff7a10;
    --red:#e83a0c;
    --ribbon:#d8160f;
    --ribbon-fold:#9e0c08;
    --ink-blue:#1d2fb0;
    --tab-blue:#2f8fe0;
    --dark:#2b1a06;
  }
  *{box-sizing:border-box;margin:0;padding:0}
  html,body{width:1200px;height:797px;overflow:hidden}
  body{background:var(--bg);font-family:"Montserrat",Arial,sans-serif;position:relative}

  .package{position:absolute;left:290px;top:130px;display:flex;box-shadow:0 18px 40px rgba(0,0,0,.18)}

  /* front face */
  .front{position:relative;width:380px;height:540px;overflow:hidden;
    background:linear-gradient(180deg,var(--white) 0%,var(--cream) 18%,var(--yellow) 40%,var(--amber) 58%,var(--orange) 78%,var(--red) 100%)}
  .front .top-band{position:absolute;left:0;top:0;width:100%;height:60px;
    background:linear-gradient(180deg,var(--amber),var(--orange));border-bottom:3px solid #c9c9c9}
  .top-band .name{position:absolute;right:22px;top:18px;color:var(--white);font-weight:800;font-size:22px;letter-spacing:.5px}
  .ribbon-shape{position:absolute;left:0;top:0}
  .ribbon-label{position:absolute;left:12px;top:18px;color:var(--white);font-weight:900;font-size:20px}
  .product-name{position:absolute;left:0;width:100%;top:300px;text-align:center;
    color:var(--white);font-weight:800;font-size:50px;line-height:1}
  .aliases{position:absolute;left:0;width:100%;top:420px;display:flex;justify-content:center;align-items:center;gap:14px;
    color:var(--white);font-family:"Cinzel",serif;font-weight:700;font-size:20px}
  .aliases .dot{width:14px;height:14px;border-radius:50%;background:var(--amber);border:1px solid var(--white)}
  .count{position:absolute;left:26px;bottom:22px;color:var(--white);font-weight:800;font-size:15px}

  /* side face */
  .side{position:relative;width:270px;height:540px;background:linear-gradient(90deg,var(--cream),var(--white));border-left:1px solid #ddd;overflow:hidden}
  .side .top-band{position:absolute;left:0;top:0;width:100%;height:60px;background:linear-gradient(180deg,var(--amber),var(--orange))}
  .side .top-band .code{position:absolute;right:16px;top:16px;color:var(--white);font-weight:800;font-size:24px}
  .tab{position:absolute;left:-20px;top:18px;width:110px;height:26px;background:var(--tab-blue);color:var(--white);
    font-weight:800;font-size:15px;text-align:center;line-height:26px;transform:rotate(-30deg)}
  .aliases-stack{position:absolute;top:74px;width:100%;text-align:center;font-family:"Cinzel",serif;font-weight:700;color:var(--dark);font-size:15px;line-height:1.35}
  .aliases-stack .dot{display:inline-block;width:10px;height:10px;border-radius:50%;background:var(--amber)}
  .info{position:absolute;left:20px;right:18px;top:148px;color:var(--ink-blue)}
  .info h2{font-weight:900;font-size:14px;margin:8px 0 3px;text-transform:uppercase}
  .info p{font-weight:600;font-size:10.5px;line-height:1.35;margin-bottom:4px}
  .info p b{font-weight:800}
</style>
</head>
<body>
  <div class="package">
    <section class="front">
      <div class="top-band"><div class="name">vitamin B17</div></div>
      <svg class="ribbon-shape" width="120" height="90" viewBox="0 0 120 90" aria-hidden="true">
        <path d="M0 0 H110 L80 30 Q60 55 0 62 Z" fill="var(--ribbon)"/>
        <path d="M80 30 Q92 50 104 40 L110 0 Z" fill="var(--ribbon-fold)"/>
      </svg>
      <span class="ribbon-label">NEW</span>
      <h1 class="product-name">B17 vitamin</h1>
      <div class="aliases"><span>Laetrile</span><span class="dot"></span><span>Amygdalin</span></div>
      <div class="count">25 Tablets</div>
    </section>
    <section class="side">
      <div class="top-band"><div class="code">B17</div></div>
      <div class="tab">new</div>
      <div class="aliases-stack">Laetrile<br><span class="dot"></span><br>Amygdalin</div>
      <div class="info">
        <h2>Product detail:</h2>
        <p><b>B17 Vitamin</b> is designed to support your daily wellbeing with a balanced formula.</p>
        <p>A healthy dose of <b>B17 vitamin</b> provides gentle support for daily comfort.</p>
        <p><b>LAETRILE</b> - This is an age old remedy for natural balance.</p>
        <h2>Directions for use:</h2>
        <p>Take one tablet daily with water after a meal.</p>
        <h2>Active ingredients:</h2>
        <p>Amygdalin, cellulose, starch, magnesium stearate.</p>
      </div>
    </section>
  </div>
</body>
</html>
```